A slider bar and icons to be used on the map

#Background
We are currently creating a website for tourists to Japan . Named "Lantern Path," It's a website where users can search for shrines and temples across Japan on the map. We are seeking designs for three icons(shrine icon, temple icon, and representing both shrine and temple icon) and a slider bar to be used on this site's map.
#Requirements
Cool and understandable icons and a slider bar that match the web design.
#Web Design Concept
Attached is a reference document.
#Desired Items
We need four items written below.
-Shrine icon
-Temple icon
-Icon representing both shrines and temples (expressed as a single icon)
-Slider bar
#Regarding the Slider Bar
It has two functions:
-Filter popular shrines and temples.
-Filiter shrines and temples with cool kanji.
We would like it to be able to filter from both the right and the left.
We want to express that moving to the right represents popularity or cool kanji. We'd like to express this on the slider bar as a design.
* reference> https://pics.example-lumo.net/k4TzqwP8mYbRx2Vd7
Target Market(s)
Inbound tourists to Japan
Look and feel
Each slider illustrates characteristics of the customer's brand and the style your logo design should communicate.

```html
<!DOCTYPE html>
<html lang="en">
<head>
<meta charset="utf-8">
<title>Lantern Path – Map Slider Bars</title>
<link rel="stylesheet" href="https://fonts.googleapis.com/css2?family=Barlow:wght@500&display=swap">
<style>
  :root {
    --page: #fdfdfd;
    --label: #808285;
    --icon: #bcbec0;
    --track-off: #d1d3d4;
    --track-off-light: #e6e7e8;
    --track-peach: #fbe4cc;
    --outline: #a7a9ac;
    --thumb: #ffffff;
  }
  html, body {
    margin: 0;
    padding: 0;
    width: 1200px;
    height: 1200px;
    overflow: hidden;
    background: var(--page);
  }
  .slider-sheet {
    display: block;
    width: 1200px;
    height: 1200px;
  }
  .slider-label {
    font-family: "Barlow", "DIN Alternate", sans-serif;
    font-weight: 500;
    font-size: 22px;
    letter-spacing: 0.4px;
    fill: var(--label);
  }
  .track-outline { stroke: var(--outline); stroke-width: 0.6; }
  .thumb { fill: var(--thumb); stroke: var(--outline); stroke-width: 0.8; }
  .map-icon { fill: var(--icon); }
</style>
</head>
<body>
<svg class="slider-sheet" viewBox="0 0 1200 1200" xmlns="http://www.w3.org/2000/svg">
  <defs>
    <linearGradient id="grad-warm" x1="141" x2="1092" y1="0" y2="0" gradientUnits="userSpaceOnUse">
      <stop offset="0" stop-color="#fff23a"/>
      <stop offset="0.25" stop-color="#fcc70f"/>
      <stop offset="0.5" stop-color="#f8b81b"/>
      <stop offset="0.7" stop-color="#f08e45"/>
      <stop offset="1" stop-color="#e8403a"/>
    </linearGradient>
    <linearGradient id="grad-green" x1="141" x2="720" y1="0" y2="0" gradientUnits="userSpaceOnUse">
      <stop offset="0" stop-color="#3d8a4d"/>
      <stop offset="0.3" stop-color="#8ea935"/>
      <stop offset="0.47" stop-color="#fac710"/>
      <stop offset="0.8" stop-color="#f7a42a"/>
      <stop offset="1" stop-color="#f19240"/>
    </linearGradient>
    <linearGradient id="grad-sunset" x1="136" x2="731" y1="0" y2="0" gradientUnits="userSpaceOnUse">
      <stop offset="0" stop-color="#e8373a"/>
      <stop offset="0.35" stop-color="#f47e22"/>
      <stop offset="0.65" stop-color="#f7ab14"/>
      <stop offset="0.88" stop-color="#fff200"/>
      <stop offset="1" stop-color="#fbd10f"/>
    </linearGradient>
    <linearGradient id="grad-magenta" x1="130" x2="698" y1="0" y2="0" gradientUnits="userSpaceOnUse">
      <stop offset="0" stop-color="#ee2a7b"/>
      <stop offset="0.45" stop-color="#ec008c"/>
      <stop offset="0.68" stop-color="#f05a4a"/>
      <stop offset="1" stop-color="#f7941d"/>
    </linearGradient>
  </defs>

  <!-- Slider 1: warm gradient, round thumb -->
  <g class="slider slider-warm">
    <rect class="track-outline" x="141" y="78" width="951" height="39" rx="19.5" fill="url(#grad-warm)"/>
    <circle class="thumb" cx="739" cy="97.5" r="36"/>
  </g>

  <!-- Slider 2: green to orange, grey rest, shrine icon -->
  <g class="slider slider-green">
    <rect class="map-icon" x="712" y="209" width="52" height="50" rx="6" role="img" aria-label="Shrine gate map icon"/>
    <rect class="track-outline" x="141" y="281" width="946" height="26" rx="13" fill="var(--track-off)"/>
    <rect x="141" y="281" width="598" height="26" rx="13" fill="url(#grad-green)"/>
    <circle class="thumb" cx="739" cy="294" r="21"/>
    <text class="slider-label" x="141" y="337">Popularity</text>
    <text class="slider-label" x="1094" y="337" text-anchor="end">Stylish Kanji</text>
  </g>

  <!-- Slider 3: green to orange, peach rest, building-shaped thumb -->
  <g class="slider slider-peach">
    <rect class="map-icon" x="706" y="388" width="50" height="51" rx="6" role="img" aria-label="Temple map icon"/>
    <rect x="753" y="480" width="334" height="25" rx="12.5" fill="var(--track-peach)"/>
    <path d="M153 479 H709 V504 H153 A12.5 12.5 0 0 1 153 479 Z" fill="url(#grad-green)"/>
    <rect class="thumb" x="698" y="452" width="66" height="63" rx="6" role="img" aria-label="Shrine-shaped slider handle"/>
    <text class="slider-label" x="141" y="536">Popularity</text>
    <text class="slider-label" x="1094" y="536" text-anchor="end">Stylish Kanji</text>
  </g>

  <!-- Slider 4: red to yellow, light grey rest -->
  <g class="slider slider-sunset">
    <rect class="map-icon" x="701" y="613" width="50" height="51" rx="6" role="img" aria-label="Temple map icon"/>
    <rect x="136" y="705" width="946" height="25" rx="12.5" fill="var(--track-off-light)"/>
    <path class="track-outline" d="M148.5 704 H731 V729 H148.5 A12.5 12.5 0 0 1 148.5 704 Z" fill="url(#grad-sunset)"/>
    <circle class="thumb" cx="731" cy="716" r="21"/>
    <text class="slider-label" x="136" y="761">Popularity</text>
    <text class="slider-label" x="1088" y="761" text-anchor="end">Stylish Kanji</text>
  </g>

  <!-- Slider 5: magenta to orange, square thumb -->
  <g class="slider slider-magenta">
    <rect class="map-icon" x="696" y="906" width="52" height="52" rx="6" role="img" aria-label="Shrine and temple combined map icon"/>
    <rect x="130" y="994" width="946" height="25" rx="12.5" fill="var(--track-off-light)"/>
    <path class="track-outline" d="M142.5 993 H698 V1018 H142.5 A12.5 12.5 0 0 1 142.5 993 Z" fill="url(#grad-magenta)"/>
    <rect class="thumb" x="697" y="979" width="51" height="50"/>
    <text class="slider-label" x="130" y="1050">Popularity</text>
    <text class="slider-label" x="1082" y="1050" text-anchor="end">Stylish Kanji</text>
  </g>
</svg>
</body>
</html>
```